Flyer

I am a qualified accountant and I need a flyer to promote my business when networking

My services include
Management Accounts, Financial Accounts, Day to Day Bookkeeping services, business start up assistance
I will produce and submit Self Assessment Tax Returns, Annual Accounts, VAT tax returns, Payroll and PAYE

I attach my business card design so that there is some continuity if you think it appropiate.

Size A3 is preferred, please.

Sorry, I mean't Size A5 is preferred.

A5 please

Free initial consultations and advice.

```html
<!DOCTYPE html>
<html lang="en">
<head>
<meta charset="utf-8">
<title>Clara Webb Accounting – Flyer</title>
<link rel="stylesheet" href="https://fonts.googleapis.com/css2?family=Goudy+Bookletter+1911&family=Open+Sans:wght@500&display=swap">
<style>
  :root {
    --paper: #ffffff;
    --green-bright: #3af50a;
    --green-lime: #9dfc00;
    --yellow-lime: #c6f500;
    --pale-lime: #e4fbb0;
    --pale-mint: #eafcd6;
    --ink-green: #3c8c1c;
    --ink-dark: #1c1c1c;
  }
  * { margin: 0; padding: 0; box-sizing: border-box; }
  html, body { width: 847px; height: 1200px; overflow: hidden; background: var(--paper); }
  .flyer {
    position: relative;
    width: 847px;
    height: 1200px;
    overflow: hidden;
    background: var(--paper);
    font-family: "Goudy Bookletter 1911", serif;
    color: var(--ink-green);
  }
  .flyer__backdrop { position: absolute; inset: 0; width: 847px; height: 1200px; }
  .brand {
    position: absolute;
    left: 0; top: 0;
    width: 847px;
    height: 300px;
  }
  .brand__name {
    position: absolute;
    left: 74px; top: 128px;
    font-size: 26px;
    letter-spacing: 1.5px;
    color: var(--ink-dark);
    text-transform: uppercase;
    white-space: nowrap;
  }
  .brand__tagline {
    position: absolute;
    left: 176px; top: 162px;
    font-family: "Open Sans", sans-serif;
    font-weight: 500;
    font-size: 15px;
    color: var(--ink-dark);
    white-space: nowrap;
  }
  .services {
    position: absolute;
    left: 0; top: 372px;
    width: 847px;
    text-align: center;
  }
  .services__title { font-size: 38px; font-weight: normal; line-height: 46px; margin-bottom: 28px; }
  .services__list { list-style: none; font-size: 30px; line-height: 40.5px; }
  .contact {
    position: absolute;
    left: 0; top: 835px;
    width: 847px;
    text-align: center;
    font-size: 28px;
    line-height: 37px;
  }
  .contact a { color: inherit; text-decoration: none; }
  .signature {
    position: absolute;
    left: 52px; top: 1097px;
    font-size: 30px;
    white-space: nowrap;
  }
</style>
</head>
<body>
<main class="flyer">
  <svg class="flyer__backdrop" viewBox="0 0 847 1200" aria-hidden="true">
    <defs>
      <linearGradient id="field" x1="0" y1="0" x2="1" y2="0.7">
        <stop offset="0" stop-color="var(--green-bright)"/>
        <stop offset="0.55" stop-color="var(--green-lime)"/>
        <stop offset="1" stop-color="var(--yellow-lime)"/>
      </linearGradient>
      <linearGradient id="fade" x1="0" y1="0" x2="1" y2="1">
        <stop offset="0" stop-color="var(--pale-lime)"/>
        <stop offset="1" stop-color="var(--pale-mint)"/>
      </linearGradient>
    </defs>
    <polygon class="band band--pale" points="0,480 847,700 847,900 760,890 690,1010 455,1020 0,590" fill="url(#fade)" opacity="0.9"/>
    <polygon class="band band--soft" points="0,480 847,690 847,790 770,780 0,560" fill="var(--yellow-lime)" opacity="0.45"/>
    <polygon class="band band--main" points="0,0 847,0 847,678 0,468" fill="url(#field)"/>
    <polygon class="band band--light" points="0,0 70,0 70,95 0,120" fill="var(--paper)" opacity="0.55"/>
    <polygon class="brand__panel" points="74,94 300,0 456,189 226,283" fill="var(--paper)"/>
  </svg>

  <header class="brand">
    <p class="brand__name">Clara Webb Accounting</p>
    <p class="brand__tagline">Making Accounts look easy</p>
  </header>

  <section class="services">
    <h2 class="services__title">Services Include:</h2>
    <ul class="services__list">
      <li>Management Accounts</li>
      <li>Fainancial Accounts</li>
      <li>Bookkeeping Services</li>
      <li>Bussiness Start up Assistance</li>
      <li>Produce And Submit : Self Assessment Tax</li>
      <li>Returns ,Annual Accounts ,Vat Returns ,</li>
      <li>Payroll And PAYE.</li>
    </ul>
  </section>

  <address class="contact" style="font-style: normal;">
    <a href="mailto:clara@clarawebbaccounts.com">clara@clarawebbaccounts.com</a><br>
    07700 900418
  </address>

  <p class="signature">Clara Webb ACMA, CGMA</p>
</main>
</body>
</html>
```